Recipe Card Design

I have a small kitchen store in Livingston Montana, and I would like to have recipe cards (4x6 postcard) designed with my logo, lines for recipe writing, all in black and white. My website is here: www.brambleforkpantry.com

Store

```html
<!DOCTYPE html>
<html lang="en">
<head>
<meta charset="utf-8">
<title>Bramblefork Pantry – Recipe Card</title>
<link rel="stylesheet" href="https://fonts.googleapis.com/css2?family=Cinzel:wght@700&family=Amatic+SC:wght@700&display=swap">
<style>
  :root {
    --board: #1b1b1b;
    --board-edge: #111;
    --paper: #ffffff;
    --ink: #111111;
    --rule: #444444;
    --art-light: #d9d9d9;
    --art-dark: #2a2a2a;
    --page: #ffffff;
  }
  * { box-sizing: border-box; margin: 0; padding: 0; }
  html, body { width: 1200px; height: 1200px; overflow: hidden; background: var(--page); }
  .canvas { position: relative; width: 1200px; height: 1200px; }

  .card {
    position: absolute; left: 14px; top: 150px; width: 1172px; height: 898px;
    background: radial-gradient(circle at 40% 30%, #262626, var(--board) 70%);
    border: 1px solid var(--board-edge);
  }

  .brand {
    position: absolute; left: 56px; top: 37px; width: 228px; height: 285px;
    display: flex; align-items: center; justify-content: center; gap: 12px;
    flex-direction: column;
  }
  .brand-mark { width: 34px; height: 34px; border: 3px solid var(--paper); }
  .brand-name {
    font-family: "Cinzel", serif; font-weight: 700; font-size: 34px; line-height: 1.15;
    color: var(--paper); text-align: center; text-transform: uppercase;
  }

  .title-word {
    position: absolute; left: 60px; top: 352px; width: 118px; height: 234px;
    display: flex; align-items: center; justify-content: center;
  }
  .title-word span {
    transform: rotate(-90deg); white-space: nowrap;
    font-family: "Amatic SC", sans-serif; font-weight: 700; font-size: 150px;
    letter-spacing: 4px; color: var(--paper); line-height: 1;
  }

  .title-ribbon { position: absolute; left: 196px; top: 352px; width: 110px; height: 498px; }

  .art { position: absolute; border-radius: 10px; }
  .art-utensils { left: 66px; top: 614px; width: 108px; height: 116px; background: linear-gradient(135deg, var(--art-light), #9a9a9a); opacity: .85; }
  .art-pie { left: 60px; top: 766px; width: 114px; height: 64px; border-radius: 50%; background: linear-gradient(180deg, var(--art-light), #8a8a8a); opacity: .85; }

  .panel {
    position: absolute; background: var(--paper);
    border-radius: 16px; outline: 4px dotted var(--paper); outline-offset: 1px;
  }
  .panel-ingredients { left: 351px; top: 32px; width: 728px; height: 276px; }
  .panel-instructions { left: 356px; top: 384px; width: 726px; height: 468px; }

  .panel-heading {
    position: absolute; top: 38px; left: 0; right: 0;
    display: flex; justify-content: center; align-items: flex-end; gap: 8px;
  }
  .flourish { width: 114px; height: 16px; border-radius: 8px; background: linear-gradient(90deg, transparent, #555); margin-bottom: 2px; }
  .panel-heading h2 {
    font-family: "Cinzel", serif; font-weight: 700; font-size: 30px; color: var(--ink);
    letter-spacing: 0.5px; line-height: 1;
  }
  .panel-heading h2::first-letter { font-size: 40px; }

  .rules { position: absolute; list-style: none; }
  .rules li { height: 0; border-top: 1.5px dotted var(--rule); }
  .panel-ingredients .rules { left: 57px; top: 111px; width: 632px; }
  .panel-ingredients .rules li { margin-bottom: 32.5px; }
  .panel-instructions .rules { left: 52px; top: 106px; width: 573px; }
  .panel-instructions .rules li { margin-bottom: 29.8px; }

  .art-tools { left: 588px; top: 294px; width: 140px; height: 172px; background: linear-gradient(160deg, #bdbdbd, var(--art-dark)); }

  .divider {
    position: absolute; left: 351px; top: 338px; width: 723px; height: 0;
    border-top: 4px dotted var(--paper);
  }
</style>
</head>
<body>
<main class="canvas">
  <section class="card">
    <div class="brand">
      <div class="brand-mark"></div>
      <div class="brand-name">Bramblefork<br>Pantry</div>
    </div>

    <div class="title-word"><span>RECEPE</span></div>
    <svg class="title-ribbon" viewBox="0 0 110 498" aria-hidden="true">
      <polygon points="0,0 55,22 110,0 110,498 55,474 0,498" fill="#ffffff"/>
    </svg>

    <div class="art art-utensils" role="img" aria-label="Crossed fork and spoon illustration"></div>
    <div class="art art-pie" role="img" aria-label="Lattice-top pie illustration"></div>

    <div class="panel panel-ingredients">
      <div class="panel-heading">
        <div class="flourish" role="img" aria-label="Calligraphic flourish"></div>
        <h2>Ingredients</h2>
      </div>
      <ul class="rules"><li></li><li></li><li></li><li></li><li></li></ul>
    </div>

    <div class="divider"></div>

    <div class="panel panel-instructions">
      <div class="panel-heading">
        <div class="flourish" role="img" aria-label="Calligraphic flourish"></div>
        <h2>Instruction</h2>
      </div>
      <ul class="rules">
        <li></li><li></li><li></li><li></li><li></li><li></li>
        <li></li><li></li><li></li><li></li><li></li><li></li>
      </ul>
      <div class="art art-tools" role="img" aria-label="Oven mitt and box grater illustration"></div>
    </div>
  </section>
</main>
</body>
</html>
```